Meadow Lark Roasters (coffee packaging design)

Project Overview:
🔥 Attention for Designer

You have been provided with detailed brand files, fonts, and reference designs for a reason. I expect work that is better than what I could create myself. The design should be thoughtful, professional, and aligned with our brand identity.

Read the full project description carefully. Every detail matters. If something is unclear, ask questions before starting. Do not just drop logos or assets onto a layout. Understand the intent and build something that fits the vision.

Rushed or mediocre work will not be accepted. I want quality over quantity with real creative thinking and brand awareness behind it.
We’re creating a high-end yet playful packaging design for Meadow Lark Roasters, intended to reflect the classy and nature-inspired feel of Pine Hollow(pinehollowyardplay.example) while adding a touch of lighthearted charm.

Design Elements to Include

Logo & Brand Cues: Incorporate the Pine Hollow logo (round circle with dog head) and use our established color palette and leafy, forestry brand patterns. This will ensure consistency and a high-end feel.

Doodle Elements (Optional): If it suits the design, feel free to incorporate the doodle-style handwriting and sketches that appear on our website (like dog names or playful notes). This adds a personal and approachable touch, though it’s not mandatory.

Bag Format: Design for a 16 oz bag, with the option to either do a full custom print or a high-quality branded sticker on a neutral bag. The goal is to make the packaging feel special and on-brand.

Overall Vibe
Think modern, classy, and a little bit whimsical. The packaging should look polished enough to be a premium product while still capturing the fun, dog-friendly personality of Pine Hollow.
Needs: its own special logo something that can be put on cups, and stickers. We also want the bag design to feel special and not just a logo slapped onto a coffee bag, so in a way i want 2 deliverables.

fonts: in the files uploaded

Target Market(s)

Dog Owners

Font styles to use
Other font styles liked:
• Fonts are in files

Requirements
Must have
• Use our brand guidelines

```html
<!DOCTYPE html>
<html lang="en">
<head>
<meta charset="utf-8">
<title>Meadow Lark Roasters – Bag Front</title>
<link rel="stylesheet" href="https://fonts.googleapis.com/css2?family=Poppins:wght@500;800&family=Gochi+Hand&display=swap">
<style>
  :root {
    --backdrop: #f3f0e9;
    --bag-brown: #4f4538;
    --bag-brown-dark: #3b3329;
    --bag-brown-light: #6a5d4b;
    --leaf-lime: #bccb3c;
    --label-cream: #fbf0d3;
    --label-cream-light: #fdf6e3;
    --ink-brown: #4a3f33;
    --mark-brown: #6b5a48;
    --art-sand: #e8d6a4;
    --art-green: #a9bc36;
  }
  * { margin: 0; padding: 0; box-sizing: border-box; }
  html, body {
    width: 885px;
    height: 1200px;
    overflow: hidden;
    background: var(--backdrop);
  }
  .canvas {
    position: relative;
    width: 885px;
    height: 1200px;
  }
  .bag-front {
    position: absolute;
    left: 112px;
    top: 40px;
    width: 660px;
    height: 1120px;
  }
  .forest-pattern {
    position: absolute;
    inset: 0;
    border-radius: 6px;
    background:
      radial-gradient(circle at 25% 20%, rgba(188, 203, 60, 0.22), transparent 45%),
      radial-gradient(circle at 80% 75%, rgba(188, 203, 60, 0.18), transparent 50%),
      linear-gradient(160deg, var(--bag-brown-light), var(--bag-brown) 45%, var(--bag-brown-dark));
  }
  .label-shape {
    position: absolute;
    inset: 0;
  }
  .brand-mark {
    position: absolute;
    left: 0;
    width: 660px;
    top: 250px;
    text-align: center;
  }
  .brand-mark__dot {
    display: block;
    width: 150px;
    height: 150px;
    margin: 0 auto;
    border-radius: 50%;
    background: var(--mark-brown);
  }
  .brand-mark__name {
    display: block;
    margin-top: 16px;
    font-family: "Poppins", sans-serif;
    font-weight: 500;
    font-size: 26px;
    letter-spacing: 6px;
    color: var(--mark-brown);
    text-transform: uppercase;
  }
  .product-title {
    position: absolute;
    left: 0;
    width: 660px;
    top: 560px;
    text-align: center;
    font-family: "Poppins", sans-serif;
    color: var(--ink-brown);
    line-height: 1.05;
  }
  .product-title__main {
    display: block;
    font-weight: 800;
    font-size: 54px;
    letter-spacing: 1px;
  }
  .product-title__sub {
    display: block;
    font-weight: 500;
    font-size: 48px;
    letter-spacing: 1px;
  }
  .tagline {
    position: absolute;
    left: 0;
    width: 660px;
    top: 730px;
    text-align: center;
    font-family: "Gochi Hand", cursive;
    font-size: 32px;
    line-height: 1.3;
    color: var(--ink-brown);
  }
  .dog-scene {
    position: absolute;
    left: 90px;
    top: 880px;
    width: 480px;
    height: 150px;
    border-radius: 4px;
    background: linear-gradient(90deg, var(--art-green) 0%, var(--art-green) 22%, var(--art-sand) 34%, var(--art-sand) 70%, var(--mark-brown) 82%, var(--label-cream) 100%);
    opacity: 0.85;
  }
</style>
</head>
<body>
<main class="canvas">
  <section class="bag-front">
    <div class="forest-pattern" role="img" aria-label="Leafy forest pattern of lime and sand leaves and sprigs on dark brown"></div>

    <svg class="label-shape" width="660" height="1120" viewBox="0 0 660 1120" aria-hidden="true">
      <defs>
        <linearGradient id="labelFill" x1="0" y1="0" x2="0" y2="1">
          <stop offset="0" stop-color="#fdf6e3"/>
          <stop offset="1" stop-color="#f9ecc9"/>
        </linearGradient>
      </defs>
      <path d="M70,420 H160 V390 A170,170 0 0 1 500,390 V420 H590 V1050 H70 Z"
            fill="url(#labelFill)" stroke="#bccb3c" stroke-width="8" stroke-linejoin="round"/>
      <path d="M82,432 H172 V390 A158,158 0 0 1 488,390 V432 H578 V1038 H82 Z"
            fill="none" stroke="#d4dd7a" stroke-width="2"/>
    </svg>

    <div class="brand-mark">
      <span class="brand-mark__dot"></span>
      <span class="brand-mark__name">Pine Hollow</span>
    </div>

    <h1 class="product-title">
      <span class="product-title__main">MEADOW LARK</span>
      <span class="product-title__sub">ROASTERS</span>
    </h1>

    <p class="tagline">Because great days<br>start with a great brew<br>and a happy dog.</p>

    <div class="dog-scene" role="img" aria-label="Illustration of two dogs sitting with cups of coffee beside a green box"></div>
  </section>
</main>
</body>
</html>
```